New name flyer

We have just changed our business name from kR Property group to Harbour Lantern. We want to distribute a flyer to the local community to inform them of the change. We are a realestate agency which focuses mainly on property management but also sales. We service from Brisbane to the Sunshine coast.

Target Market(s)

Local community

Industry/Entity Type

realestate

Requirements
Must have
• Details of name change
Nice to have
• Servicing area Brisbane and Sunshine Coast, no change in management or services we offer, and will continue pride ourselves on offering a high level of service, with the same team from the Gold to Sunshine Coast.
Should not have
• too much wording.

```html
<!DOCTYPE html>
<html lang="en">
<head>
<meta charset="utf-8">
<title>Harbour Lantern – New Name Flyer</title>
<link rel="stylesheet" href="https://fonts.googleapis.com/css2?family=Montserrat:wght@400;500;700;800&family=Oswald:wght@600;700&family=Poppins:wght@700&display=swap">
<style>
  :root {
    --red: #e31e24;
    --navy: #0c2d62;
    --hero-top: #13258a;
    --hero-bottom: #3b2f80;
    --gold: #cc9a35;
    --grey-text: #555555;
    --white: #ffffff;
  }
  * { margin: 0; padding: 0; box-sizing: border-box; }
  html, body {
    width: 901px; height: 1200px; overflow: hidden;
    background: var(--white);
  }
  .flyer {
    position: absolute; left: 27px; top: 0;
    width: 1316px; height: 1864px;
    transform: scale(0.6438); transform-origin: top left;
    background: var(--white);
  }
  .flyer > * { position: absolute; }

  .announce-bar {
    left: 52px; top: 53px; width: 1208px; height: 126px;
    background: var(--red);
    display: flex; align-items: center; justify-content: center;
    font: 700 62px/1 "Oswald", sans-serif; color: var(--white);
    letter-spacing: 0.5px;
  }

  .hero {
    left: 52px; top: 179px; width: 1208px; height: 576px;
    background: linear-gradient(180deg, var(--hero-top) 0%, #1c2675 55%, var(--hero-bottom) 100%);
  }
  .old-name {
    left: 52px; top: 250px; width: 1208px; text-align: center;
    font: 500 60px/1 "Montserrat", sans-serif; color: var(--white);
    letter-spacing: 2px;
  }
  .now-label {
    left: 52px; top: 405px; width: 1208px; text-align: center;
    font: 700 70px/1 "Oswald", sans-serif; color: var(--gold);
  }
  .rule {
    height: 6px; border-top: 1.5px solid #d8dcef; border-bottom: 1.5px solid #d8dcef;
  }
  .rule-left { left: 246px; top: 443px; width: 312px; }
  .rule-right { left: 755px; top: 443px; width: 313px; }
  .rule-bottom { left: 246px; top: 696px; width: 809px; }
  .new-name {
    left: 52px; top: 512px; width: 1208px; text-align: center;
    font: 800 82px/1 "Montserrat", sans-serif; color: var(--white);
  }
  .new-descriptor {
    left: 52px; top: 612px; width: 1208px; text-align: center;
    font: 500 40px/1 "Montserrat", sans-serif; color: var(--gold);
    letter-spacing: 0.45em; padding-left: 0.45em;
  }

  .area-intro {
    left: 445px; top: 800px; width: 477px; height: 68px;
    background: var(--navy); transform: skewX(-15deg);
  }
  .area-intro span {
    display: block; transform: skewX(15deg);
    font: 400 40px/68px "Montserrat", sans-serif; color: var(--white); text-align: center;
  }
  .area-band {
    left: 296px; top: 868px; width: 778px; height: 68px;
    background: var(--gold); transform: skewX(-15deg);
  }
  .area-band span {
    display: block; transform: skewX(15deg);
    font: 700 38px/70px "Poppins", sans-serif; color: var(--white); text-align: center;
  }

  .services { left: 52px; top: 995px; width: 1208px; height: 260px; }
  .service {
    position: absolute; top: 0; width: 280px; margin-left: -140px;
    text-align: center;
  }
  .service svg { display: block; margin: 17px auto 0; }
  .service-label {
    margin-top: 30px;
    font: 700 70px/1 "Oswald", sans-serif; color: var(--grey-text);
  }
  .divider {
    position: absolute; top: 0; height: 250px; border-left: 2px dotted #777;
  }

  .photo { top: 1306px; width: 282px; height: 208px; }
  .photo-home { left: 52px; background: linear-gradient(180deg, #5d93d6 0%, #b9c7cf 50%, #5e8a3c 100%); }
  .photo-agent { left: 358px; background: linear-gradient(135deg, #e9e6e1 0%, #b8a99a 50%, #27324a 100%); }
  .photo-villa { left: 664px; background: linear-gradient(180deg, #49a6d6 0%, #d7d9d8 50%, #22b7c9 100%); }
  .photo-handover { left: 970px; background: linear-gradient(135deg, #e8e2dc 0%, #c49a7a 50%, #8a5a3c 100%); }

  .footer-brand {
    left: 52px; top: 1542px; width: 497px; height: 270px;
    background: var(--navy);
    display: flex; flex-direction: column; justify-content: center; padding-left: 86px;
  }
  .footer-brand-name {
    font: 700 48px/1.05 "Montserrat", sans-serif; color: var(--white); letter-spacing: 1px;
  }
  .footer-contact {
    left: 549px; top: 1542px; width: 711px; height: 270px;
    background: var(--gold);
    padding-left: 78px; padding-top: 72px;
  }
  .contact-phone {
    display: flex; align-items: center; gap: 22px;
    font: 800 70px/1 "Montserrat", sans-serif; color: var(--white);
  }
  .contact-web {
    display: flex; align-items: center; gap: 22px; margin-top: 28px;
    font: 400 34px/1 "Montserrat", sans-serif; color: var(--white);
  }
  .contact-web b { font-weight: 700; }
</style>
</head>
<body>
<div class="flyer">
  <div class="announce-bar">WE HAVE JUST CHANGED YOUR BUSINESS NAME</div>

  <div class="hero" role="img" aria-label="Photo of a large two-storey house with a pool at dusk"></div>
  <div class="old-name">kR PROPERTY GROUP</div>
  <div class="rule rule-left"></div>
  <div class="now-label">Now</div>
  <div class="rule rule-right"></div>
  <div class="new-name">HARBOUR LANTERN</div>
  <div class="new-descriptor">ESTATE AGENTS</div>
  <div class="rule rule-bottom"></div>

  <div class="area-intro"><span>We service from</span></div>
  <div class="area-band"><span>Brisbane to the Sunshine coast</span></div>

  <div class="services">
    <div class="divider" style="left:283px"></div>
    <div class="divider" style="left:568px"></div>
    <div class="divider" style="left:833px"></div>

    <div class="service" style="left:173px">
      <svg width="104" height="118" viewBox="0 0 104 118" aria-hidden="true">
        <polygon points="52,0 104,30 104,88 52,118 0,88 0,30" fill="#0c2d62"/>
        <path d="M26 58 L52 36 L78 58 M32 54 V80 H72 V54" fill="none" stroke="#fff" stroke-width="2.5"/>
        <text x="52" y="74" text-anchor="middle" font-family="Oswald, sans-serif" font-size="14" fill="#fff">SELL</text>
      </svg>
      <div class="service-label">SELL</div>
    </div>
    <div class="service" style="left:423px">
      <svg width="104" height="118" viewBox="0 0 104 118" aria-hidden="true">
        <polygon points="52,0 104,30 104,88 52,118 0,88 0,30" fill="#0c2d62"/>
        <circle cx="52" cy="44" r="7" fill="none" stroke="#fff" stroke-width="2.5"/>
        <path d="M52 51 V66 M52 60 H57 M34 76 Q44 70 52 74 H64 Q70 74 74 70" fill="none" stroke="#fff" stroke-width="2.5"/>
      </svg>
      <div class="service-label">LEASE</div>
    </div>
    <div class="service" style="left:710px">
      <svg width="104" height="118" viewBox="0 0 104 118" aria-hidden="true">
        <polygon points="52,0 104,30 104,88 52,118 0,88 0,30" fill="#0c2d62"/>
        <path d="M28 58 L50 38 L72 58 M34 54 V80 H56" fill="none" stroke="#fff" stroke-width="2.5"/>
        <circle cx="66" cy="72" r="9" fill="none" stroke="#fff" stroke-width="2.5"/>
        <text x="66" y="77" text-anchor="middle" font-family="Montserrat, sans-serif" font-size="12" fill="#fff">$</text>
      </svg>
      <div class="service-label">BUY</div>
    </div>
    <div class="service" style="left:998px">
      <svg width="104" height="118" viewBox="0 0 104 118" aria-hidden="true">
        <polygon points="52,0 104,30 104,88 52,118 0,88 0,30" fill="#0c2d62"/>
        <path d="M26 58 L52 36 L78 58 M32 54 V80 H72 V54" fill="none" stroke="#fff" stroke-width="2.5"/>
        <path d="M48 78 L72 54 M38 62 H46 V70 H38 Z" fill="none" stroke="#fff" stroke-width="2.5"/>
      </svg>
      <div class="service-label">DEVELOP</div>
    </div>
  </div>

  <div class="photo photo-home" role="img" aria-label="Photo of a two-storey family home with lawn"></div>
  <div class="photo photo-agent" role="img" aria-label="Photo of an agent holding up house keys and a small model house"></div>
  <div class="photo photo-villa" role="img" aria-label="Photo of a modern white house with a swimming pool"></div>
  <div class="photo photo-handover" role="img" aria-label="Photo of an agent handing keys to a couple"></div>

  <div class="footer-brand">
    <div class="footer-brand-name">HARBOUR<br>LANTERN</div>
  </div>
  <div class="footer-contact">
    <div class="contact-phone">
      <svg width="44" height="44" viewBox="0 0 24 24" aria-hidden="true">
        <path d="M6.6 10.8a15 15 0 0 0 6.6 6.6l2.2-2.2a1 1 0 0 1 1-.25 11.4 11.4 0 0 0 3.6.6 1 1 0 0 1 1 1V20a1 1 0 0 1-1 1A17 17 0 0 1 3 4a1 1 0 0 1 1-1h3.5a1 1 0 0 1 1 1c0 1.25.2 2.45.6 3.6a1 1 0 0 1-.25 1z" fill="#fff"/>
      </svg>
      <span>07 3555 0182</span>
    </div>
    <div class="contact-web">
      <svg width="44" height="44" viewBox="0 0 44 44" aria-hidden="true">
        <circle cx="22" cy="22" r="20" fill="none" stroke="#fff" stroke-width="2"/>
        <circle cx="22" cy="22" r="12" fill="none" stroke="#fff" stroke-width="1.8"/>
        <ellipse cx="22" cy="22" rx="5" ry="12" fill="none" stroke="#fff" stroke-width="1.8"/>
        <path d="M10 22 H34 M12 16 H32 M12 28 H32" stroke="#fff" stroke-width="1.5"/>
      </svg>
      <span>www.<b>harbourlantern</b>.com.au</span>
    </div>
  </div>
</div>
</body>
</html>
```